Real Estate Entrepreneur needs a business card

I am a real estate entrepreneur, I buy houses for investment purposes, I act as a real estate agent representing buyers and sellers in residential home transactions, I am a contractor that does a wide range of home repairs and construction. I'd like a design that can stick with me through the years as my business grows and morphs to fit any niche I decide to pursue as markets change.

Target Market(s)

Anyone with interest that may be related to real estate.

Industry/Entity Type

Real Estate

Contact Information for Business Card

A card that stands out and doesn't put me in any one box. My business will evolve over time and I need a card that can stay relevant.

Colors

Designer to choose colors to be used in the design.

Requirements
Must have
• Character
Nice to have
• I'm open
Should not have
• Cliche houses and hammers

```html
<!DOCTYPE html>
<html lang="en">
<head>
<meta charset="utf-8">
<title>Reid Carver – Business Card</title>
<link rel="stylesheet" href="https://fonts.googleapis.com/css2?family=Ubuntu:wght@400;500;700&display=swap">
<style>
  :root {
    --canvas-top: #e6e9eb;
    --canvas-bottom: #f7f8f9;
    --card: #2f2f30;
    --card-band: #2b2b2c;
    --band-line: #5a5a5a;
    --accent: #f2ab27;
    --text: #ffffff;
    --shadow: rgba(0, 0, 0, 0.45);
  }
  * { box-sizing: border-box; margin: 0; padding: 0; }
  html, body {
    width: 1200px;
    height: 2400px;
    overflow: hidden;
  }
  body {
    position: relative;
    background: linear-gradient(180deg, var(--canvas-top), var(--canvas-bottom));
    font-family: "Ubuntu", sans-serif;
    color: var(--text);
  }
  .card {
    position: absolute;
    left: 34px;
    width: 1133px;
    height: 643px;
    background: var(--card);
    box-shadow: 10px 14px 18px var(--shadow);
    overflow: hidden;
  }
  .card--front { top: 510px; }
  .card--back { top: 1247px; }

  /* Front */
  .front-notch {
    position: absolute;
    left: 504px;
    top: 0;
    width: 96px;
    height: 41px;
  }
  .identity {
    position: absolute;
    left: 115px;
    top: 262px;
  }
  .identity__name {
    font-weight: 500;
    font-size: 53px;
    line-height: 1;
    letter-spacing: 0.5px;
  }
  .identity__role {
    margin-top: 12px;
    font-size: 31px;
    line-height: 1;
    color: var(--accent);
  }
  .divider {
    position: absolute;
    left: 551px;
    top: 235px;
    width: 4px;
    height: 140px;
    background: var(--accent);
  }
  .contact-list {
    position: absolute;
    left: 629px;
    top: 242px;
    list-style: none;
  }
  .contact-list__item {
    display: flex;
    align-items: center;
    height: 49px;
    font-size: 30px;
  }
  .contact-list__icon {
    width: 26px;
    height: 26px;
    margin-right: 19px;
    flex: none;
  }
  .address-band {
    position: absolute;
    left: 0;
    top: 547px;
    width: 100%;
    height: 51px;
  }
  .address-band__cap {
    position: absolute;
    top: 0;
    height: 51px;
    background: var(--accent);
  }
  .address-band__cap--left { left: 0; width: 72px; }
  .address-band__cap--right { right: 0; width: 75px; }
  .address-band__bar {
    position: absolute;
    left: 72px;
    right: 75px;
    top: 0;
    height: 51px;
    background: var(--card-band);
    border-top: 2px solid var(--band-line);
    border-bottom: 2px solid var(--band-line);
    display: flex;
    align-items: center;
    justify-content: center;
    font-size: 29px;
    letter-spacing: 8px;
  }

  /* Back */
  .back-stripe {
    position: absolute;
    height: 48px;
    background: var(--accent);
  }
  .back-stripe--left { left: 0; top: 180px; width: 288px; }
  .back-stripe--right { right: 0; top: 410px; width: 298px; }
  .back-identity {
    position: absolute;
    left: 0;
    top: 252px;
    width: 100%;
    text-align: center;
    padding-left: 10px;
  }
  .back-identity__name {
    font-weight: 500;
    font-size: 72px;
    line-height: 1;
    letter-spacing: 1px;
  }
  .back-identity__role {
    margin-top: 12px;
    margin-right: 70px;
    font-size: 38px;
    line-height: 1;
    color: var(--accent);
  }
</style>
</head>
<body>
  <section class="card card--front" aria-label="Business card front">
    <svg class="front-notch" viewBox="0 0 96 41" aria-hidden="true">
      <polygon points="0,0 96,0 48,41" fill="var(--accent)"/>
    </svg>

    <div class="identity">
      <h1 class="identity__name">REID CARVER</h1>
      <p class="identity__role">real estate entrepreneur</p>
    </div>

    <div class="divider"></div>

    <ul class="contact-list">
      <li class="contact-list__item">
        <svg class="contact-list__icon" viewBox="0 0 24 24" aria-hidden="true">
          <path fill="var(--accent)" d="M6.6 10.8a15.1 15.1 0 0 0 6.6 6.6l2.2-2.2a1 1 0 0 1 1-.25 11.4 11.4 0 0 0 3.6.57 1 1 0 0 1 1 1V20a1 1 0 0 1-1 1A17 17 0 0 1 3 4a1 1 0 0 1 1-1h3.5a1 1 0 0 1 1 1c0 1.25.2 2.45.57 3.6a1 1 0 0 1-.25 1z"/>
        </svg>
        <span>+10 98 76 54 32 10</span>
      </li>
      <li class="contact-list__item">
        <svg class="contact-list__icon" viewBox="0 0 24 24" aria-hidden="true">
          <path fill="var(--accent)" d="M2 5h20v14H2z"/>
          <path fill="none" stroke="var(--card)" stroke-width="2" d="M2 6l10 7 10-7"/>
        </svg>
        <span>your mail@goes here</span>
      </li>
      <li class="contact-list__item">
        <svg class="contact-list__icon" viewBox="0 0 24 24" aria-hidden="true">
          <g fill="none" stroke="var(--accent)" stroke-width="2">
            <circle cx="12" cy="12" r="9"/>
            <ellipse cx="12" cy="12" rx="4" ry="9"/>
            <path d="M3 12h18M5 7h14M5 17h14"/>
          </g>
        </svg>
        <span>www.yourwebsite.com</span>
      </li>
    </ul>

    <div class="address-band">
      <div class="address-band__cap address-band__cap--left"></div>
      <p class="address-band__bar">123, your address will goes here</p>
      <div class="address-band__cap address-band__cap--right"></div>
    </div>
  </section>

  <section class="card card--back" aria-label="Business card back">
    <div class="back-stripe back-stripe--left"></div>
    <div class="back-identity">
      <h2 class="back-identity__name">REID CARVER</h2>
      <p class="back-identity__role">real estate entrepreneur</p>
    </div>
    <div class="back-stripe back-stripe--right"></div>
  </section>
</body>
</html>
```